Marlowe Holdings LLC - Business Cards

Need the following information on the cards:

Name: Dean R Vossler
Title: Chief Executive Manager

Business address:
412 N Ridgeview Lane #118
Carol Stream, Il 60412

Phone: (630) 555-0148 - Business
KPV FFL license number: 5-21-xxx-xx-xx-04519
Email: dean.vossler@marloweholdingsffl.com

Target Market(s)

Firearm owners

Industry/Entity Type

Firearms industry,

Contact Information for Business Card

Contact number, name and title, web page address, email, business address and kpv license number,

Requirements
Must have
• Name, title, business address, phone numbers, KPV license numbers, web page address and email address.
Nice to have
• Cellphone number,

```html
<!DOCTYPE html>
<html lang="en">
<head>
<meta charset="utf-8">
<title>Marlowe Holdings LLC – Business Cards</title>
<link href="https://fonts.googleapis.com/css2?family=Lato:ital,wght@0,400;0,700;1,400&display=swap" rel="stylesheet">
<style>
  :root {
    --red: #cc2a30;
    --charcoal: #1f1f1f;
    --stripe: #efefef;
    --paper: #ffffff;
    --ink-light: #f2f2f2;
  }
  * { margin: 0; padding: 0; box-sizing: border-box; }
  html, body { width: 1200px; height: 1200px; overflow: hidden; background: var(--paper); }
  body { position: relative; font-family: "Lato", sans-serif; }

  .card {
    position: absolute;
    left: 127px;
    width: 946px;
    height: 541px;
    overflow: hidden;
  }
  .card--front { top: 43px; }
  .card--back { top: 615px; }
  .card__art { position: absolute; inset: 0; width: 100%; height: 100%; display: block; }

  .brand-mark {
    position: absolute;
    transform: translate(-50%, -50%);
    display: flex;
    flex-direction: column;
    align-items: center;
    gap: 4px;
    width: 230px;
    text-align: center;
    font-family: "Lato", sans-serif;
    font-weight: 700;
    color: var(--red);
    font-size: 26px;
    line-height: 1.1;
    letter-spacing: 1px;
    white-space: nowrap;
  }
  .brand-mark__dot {
    width: 38px; height: 38px; border-radius: 50%;
    background: var(--red);
    margin-bottom: 10px;
  }
  .card--front .brand-mark { left: 200px; top: 271px; }
  .card--back .brand-mark { left: 747px; top: 271px; }

  .contact { position: absolute; color: var(--ink-light); white-space: nowrap; }
  .contact__name {
    left: 38px; top: 103px;
    font-weight: 700; font-size: 55px; letter-spacing: -0.5px;
  }
  .contact__title {
    left: 38px; top: 164px;
    font-style: italic; font-size: 29px;
  }
  .contact__details {
    left: 38px; top: 270px;
    font-size: 21px; line-height: 32px;
  }
  .contact__online {
    left: 38px; top: 446px;
    font-size: 21px; line-height: 32px;
  }
  .license {
    left: 593px; top: 14px;
    font-size: 18px; line-height: 19px;
  }
  .license__number { font-style: italic; }
</style>
</head>
<body>

<section class="card card--front" aria-label="Business card front">
  <svg class="card__art" viewBox="0 0 1524 871" preserveAspectRatio="none" aria-hidden="true">
    <defs>
      <filter id="hexShadow" x="-20%" y="-20%" width="150%" height="150%">
        <feDropShadow dx="14" dy="14" stdDeviation="8" flood-color="#000" flood-opacity="0.75"/>
      </filter>
    </defs>
    <rect width="1524" height="871" fill="var(--charcoal)"/>
    <polygon points="0,0 622,0 710,435 622,871 0,871" fill="var(--stripe)"/>
    <polygon points="0,0 596,0 684,435 596,871 0,871" fill="var(--red)"/>
    <polygon points="323,182 545,309 545,563 323,690 101,563 101,309" fill="var(--stripe)" filter="url(#hexShadow)"/>
  </svg>
  <svg class="card__art" viewBox="0 0 1524 871" preserveAspectRatio="none">
    <defs>
      <linearGradient id="dogGlowFront" x1="0" y1="0" x2="1" y2="1">
        <stop offset="0" stop-color="#6a1a1c" stop-opacity="0.35"/>
        <stop offset="1" stop-color="#3a1214" stop-opacity="0.2"/>
      </linearGradient>
    </defs>
    <rect x="740" y="30" width="784" height="820" rx="60" fill="url(#dogGlowFront)" role="img" aria-label="Large red line illustration of a standing shepherd dog"/>
  </svg>
  <div class="brand-mark">
    <span class="brand-mark__dot"></span>
    <span>MARLOWE</span>
    <span>HOLDINGS LLC</span>
  </div>
</section>

<section class="card card--back" aria-label="Business card back">
  <svg class="card__art" viewBox="0 0 1524 871" preserveAspectRatio="none" aria-hidden="true">
    <defs>
      <filter id="hexShadowBack" x="-20%" y="-20%" width="150%" height="150%">
        <feDropShadow dx="-14" dy="14" stdDeviation="8" flood-color="#000" flood-opacity="0.75"/>
      </filter>
    </defs>
    <rect width="1524" height="871" fill="var(--red)"/>
    <polygon points="0,0 934,0 851,419 943,871 0,871" fill="var(--stripe)"/>
    <polygon points="0,0 911,0 826,419 918,871 0,871" fill="var(--charcoal)"/>
    <polygon points="1203,182 1425,309 1425,563 1203,690 981,563 981,309" fill="var(--stripe)" filter="url(#hexShadowBack)"/>
  </svg>
  <svg class="card__art" viewBox="0 0 1524 871" preserveAspectRatio="none">
    <defs>
      <linearGradient id="dogGlowBack" x1="0" y1="0" x2="1" y2="1">
        <stop offset="0" stop-color="#4a1618" stop-opacity="0.3"/>
        <stop offset="1" stop-color="#2a1415" stop-opacity="0.15"/>
      </linearGradient>
    </defs>
    <rect x="0" y="50" width="780" height="821" rx="60" fill="url(#dogGlowBack)" role="img" aria-label="Faint line illustration of a standing shepherd dog"/>
  </svg>

  <p class="contact contact__name">DEAN R VOSSLER</p>
  <p class="contact contact__title">Chief Executive Manager</p>
  <p class="contact contact__details">412 N Ridgeview Lane #118<br>Carol Stream, IL 60412<br>Phone: (630) 555-0148 - Business</p>
  <p class="contact contact__online">dean.vossler@marloweholdingsffl.com<br>www.marloweholdingsffl.com</p>
  <p class="contact license">KPV FFL license number:<br><span class="license__number">5-21-xxx-xx-xx-04519</span></p>

  <div class="brand-mark">
    <span class="brand-mark__dot"></span>
    <span>MARLOWE</span>
    <span>HOLDINGS LLC</span>
  </div>
</section>

</body>
</html>
```